TK Alarm 'Welcome' Envelope

I am looking for a 'Welcome' envelope design for new customers who sign up for our Alarm Services. In this envelope we will send confidential documents that the customer will need. I want it to stand out, yet look classy.

```html
<!DOCTYPE html>
<html lang="en">
<head>
<meta charset="utf-8">
<title>TK Alarm Welcome Envelope</title>
<link href="https://fonts.googleapis.com/css2?family=Montserrat:wght@500;600;700&display=swap" rel="stylesheet">
<style>
  :root {
    --backdrop: #dcdde0;
    --navy: #034c83;
    --green: #3fbf36;
    --white: #ffffff;
    --window-line: #e1e3e6;
    --shade: #c9d6e3;
  }
  html, body {
    margin: 0;
    padding: 0;
    width: 1008px;
    height: 1200px;
    overflow: hidden;
    background: var(--backdrop);
  }
  .envelope-sheet {
    display: block;
    width: 1008px;
    height: 1200px;
    font-family: "Montserrat", sans-serif;
  }
  .flap { fill: var(--navy); }
  .envelope-body { fill: var(--white); }
  .corner-band { fill: var(--navy); }
  .brand-name { font-weight: 700; }
  .brand-name--navy { fill: var(--navy); }
  .brand-name--green { fill: var(--green); }
  .flap-kicker {
    fill: var(--white);
    font-weight: 600;
    letter-spacing: 9px;
  }
  .band-text { font-weight: 700; font-size: 14px; }
  .band-text--green { fill: var(--green); }
  .band-text--white { fill: var(--white); }
  .address-window {
    fill: var(--white);
    stroke: var(--window-line);
    stroke-width: 1.5;
  }
  .letter-title {
    fill: var(--navy);
    font-weight: 600;
    font-size: 29px;
    letter-spacing: 19px;
  }
</style>
</head>
<body>
<svg class="envelope-sheet" viewBox="0 0 1240 1476" xmlns="http://www.w3.org/2000/svg">
  <defs>
    <linearGradient id="chevronShade" x1="0" y1="0" x2="1" y2="0">
      <stop offset="0" stop-color="#ffffff"/>
      <stop offset="1" stop-color="#c9d6e3"/>
    </linearGradient>
    <linearGradient id="sceneTone" x1="0" y1="0" x2="1" y2="1">
      <stop offset="0" stop-color="#f6f6f7"/>
      <stop offset="0.5" stop-color="#e8e9eb"/>
      <stop offset="1" stop-color="#f4f4f5"/>
    </linearGradient>
  </defs>

  <!-- Front of envelope -->
  <g class="envelope-front">
    <path class="flap" d="M89 347 C95 300 110 272 160 262 L560 168 Q620 154 680 168 L1080 262 C1130 272 1145 300 1152 347 Z"/>
    <g class="flap-branding" transform="rotate(180 620 262)">
      <text class="flap-kicker" x="620" y="234" font-size="18" text-anchor="middle">WELCOME TO</text>
      <text class="brand-name brand-name--green" x="620" y="288" font-size="50" text-anchor="middle">TK Alarm</text>
    </g>

    <rect class="envelope-body" x="89" y="347" width="1063" height="461"/>

    <rect role="img" aria-label="Line illustration of a cut-away house with orange security device icons" x="450" y="355" width="670" height="390" fill="url(#sceneTone)"/>

    <polygon points="253,347 300,347 490,578 430,645 390,645 470,578" fill="url(#chevronShade)"/>
    <polygon points="253,347 470,578 390,645 89,645 89,433 338,433" fill="var(--white)" opacity="0"/>

    <polygon class="corner-band" points="89,347 253,347 338,433 89,433"/>
    <text class="band-text band-text--green" x="115" y="391">PO Box 527604</text>
    <text class="band-text band-text--green" x="115" y="407">Boise, ID 83799</text>

    <text class="brand-name brand-name--navy" x="112" y="595" font-size="46">TK Alarm</text>

    <rect class="address-window" x="203" y="628" width="447" height="112" rx="10"/>

    <polygon class="corner-band" points="89,722 320,722 253,808 89,808"/>
    <text class="band-text band-text--green" x="115" y="752">24 HOUR</text>
    <text class="band-text band-text--green" x="115" y="768">PROTECTION</text>
    <text class="band-text band-text--white" x="115" y="784">888 555 0142</text>

    <text class="letter-title" x="345" y="788">WELCOME LETTER</text>
  </g>

  <!-- Back of envelope -->
  <g class="envelope-back">
    <rect class="envelope-body" x="89" y="852" width="1063" height="461"/>
    <path class="flap" d="M89 852 C95 900 110 928 160 938 L560 1024 Q620 1040 680 1024 L1080 938 C1130 928 1145 900 1152 852 Z"/>
    <text class="flap-kicker" x="620" y="908" font-size="18" text-anchor="middle">WELCOME TO</text>
    <text class="brand-name brand-name--green" x="620" y="966" font-size="52" text-anchor="middle">TK Alarm</text>
  </g>
</svg>
</body>
</html>
```